Flyer-Design für Prozessfinanzierungsfirma
Zielgruppe
Wir sind eine Prozessfinanzierungsfirma. im Versicherungsbereich die größte Österreichs mit mehr als 50.000 Klienten und unser neues Projekt ist die Prozessfinanzierung von Patienten die durch einen Kunstfehler (Fehler von Ärzten) auf Schadenersatz klagen wollen aber nicht die Finanziellen Möglichkeiten haben.
Aufgabenstellung
Folder soll eine DIN A4 Doppelseite sein (also 4 A4 Seiten)
plus extra ein A4 Einlage Blatt Fragebogen fix vorgegebene Fragen.
#614032 Dieser Folder ist für die gleiche Firma im Bereich Versicherungen
www.wundbrief.at. TEXTE und DESIGN - FARBEN und INHALTE von dieser Homepage übernehmen
die Seite www.talbergring.at ist die gleiche Prozessfinanzierungsfirma - hier gibt es bereits einen Folder. Ich lade diesen hoch...
Diese Fragen sind unbedingt 1:1 zu übernehmen für das Einlageblatt :
o Was waren meine Erkrankungen vor der Behandlung, inkl. Dauermedikation?
o Warum ging ich zum Arzt?
o Was hat mir der Arzt empfohlen?
o Wurde ich über die unterschiedlichen Behandlungsmöglichkeiten aufgeklärt?
o Was wollte ich haben?
o Was wurde gemacht?
o Was hat der Arzt aus meiner Sicht falsch gemacht?
o Was wurde als weiterer Behandlungsweg empfohlen?
o Habe ich den Arzt mit meinem Problem konfrontiert?
o Wie hat mein Arzt darauf reagiert?
o Was ist jetzt genau schlechter als vorher?
Bei dem A4 Einlageblatt sollen auf der Vorderseite und der halben Rückseite diese Fragen mit entsprechendem Platz für den Text zum ausfüllen erscheinen und die untere Hälfte der 2. Seite mit einem kurzen Slogan nochmal auf unsere Leistung aufmerksam machen - ein Feld in Kreditkartengrösse für den Empfehlungsbgeber weiss zum einkleben einer Karte freibleiben und die Firmendaten (siehe Homepage) mit Anschrift, Telefonnummer und e-mailadresse angegeben sein

```html
<!DOCTYPE html>
<html lang="de">
<head>
<meta charset="utf-8">
<title>Fragebogen – Rückseite</title>
<link rel="stylesheet" href="https://fonts.googleapis.com/css2?family=Source+Sans+3:ital,wght@0,400;0,600;1,600&family=Kaushan+Script&display=swap">
<style>
  :root {
    --paper-grey: #ececf0;
    --field-white: #ffffff;
    --brand-red: #7b1e1e;
    --dash-red: #8a2a22;
    --text-dark: #1f1f1f;
    --logo-grey: #3a3a3a;
  }
  * { margin: 0; padding: 0; box-sizing: border-box; }
  html, body { width: 856px; height: 1200px; overflow: hidden; }
  body { font-family: "Source Sans 3", Arial, sans-serif; color: var(--text-dark); }

  .sheet { position: relative; width: 856px; height: 1200px; background: var(--paper-grey); }

  .question {
    position: absolute; left: 40px; font-size: 20px; line-height: 1;
  }
  .question::before { content: "•"; margin-right: 6px; font-size: 14px; vertical-align: 2px; }

  .answer-field {
    position: absolute; left: 65px; width: 733px; height: 74px;
    background: var(--field-white); border-radius: 0 22px 22px 0;
  }
  .answer-field::after {
    content: ""; position: absolute; left: 5px; right: 7px; top: 36px;
    border-top: 1.5px dashed var(--dash-red);
  }

  .hero {
    position: absolute; left: 0; top: 511px; width: 856px; height: 268px;
    background: linear-gradient(100deg, #2d3f7a 0%, #5a6890 22%, #c9cdd8 48%, #e4e6ec 70%, #f2f3f5 100%);
  }
  .brand {
    position: absolute; left: 575px; top: 644px;
    display: flex; align-items: center; gap: 10px;
  }
  .brand-square { width: 26px; height: 26px; border: 3px solid var(--logo-grey); }
  .brand-name { font-size: 19px; font-weight: 600; color: var(--logo-grey); letter-spacing: 0.3px; }

  .footer-band {
    position: absolute; left: 0; top: 779px; width: 856px; height: 421px;
    background: var(--brand-red); color: #fff;
  }
  .slogan {
    position: absolute; top: 22px; left: 0; width: 100%;
    text-align: center; font-family: "Kaushan Script", cursive;
    font-size: 31px; line-height: 46px; letter-spacing: 1px;
  }
  .company-data {
    position: absolute; left: 54px; top: 139px;
    font-style: italic; font-weight: 600; font-size: 20px; line-height: 26.8px;
    list-style: none;
  }
  .referral-card {
    position: absolute; left: 477px; top: 153px; width: 345px; height: 224px;
    background: var(--field-white); border-radius: 20px;
    display: flex; align-items: center; justify-content: center;
  }
  .referral-label { color: var(--brand-red); font-style: italic; font-weight: 600; font-size: 13.5px; }
</style>
</head>
<body>
<main class="sheet">
  <p class="question" style="top:40px">Was wurde als weiterer Behandlungsweg empfohlen?</p>
  <div class="answer-field" style="top:69px"></div>

  <p class="question" style="top:147px">Habe ich den Arzt mit meinem Problem konfrontiert?</p>
  <div class="answer-field" style="top:176px"></div>

  <p class="question" style="top:254px">Wie hat mein Arzt darauf reagiert?</p>
  <div class="answer-field" style="top:282px"></div>

  <p class="question" style="top:361px">Was ist jetzt genau schlechter als vorher?</p>
  <div class="answer-field" style="top:388px"></div>

  <div class="hero" role="img" aria-label="Foto: drei Ärzte in Praxiskleidung betrachten gemeinsam ein Röntgenbild"></div>
  <div class="brand">
    <span class="brand-square"></span>
    <span class="brand-name">Halvora Prozessfinanzierung</span>
  </div>

  <section class="footer-band">
    <p class="slogan">ärztliche Kunstfehler? - Ihr Recht<br>mit unserer Unterstützung sichern!</p>
    <ul class="company-data">
      <li>Halvora Prozessfinanzierung GmbH</li>
      <li>FN 382714k</li>
      <li>UID: ATU64829173</li>
      <li>Ebnergasse 12</li>
      <li>1040 Wien</li>
      <li>Tel: +43 (0)1/555 01 40</li>
      <li>Fax: +43 (0)1/555 01 40-10</li>
      <li>www.wundbrief.at</li>
      <li>office@wundbrief.at</li>
    </ul>
    <div class="referral-card"><span class="referral-label">empfohlen von</span></div>
  </section>
</main>
</body>
</html>
```